I require my existing website to be updated

I have an existing website on Squarespace. I would like to refresh it, change some of the copy, add in my new video that we created. I want to give it a new look. My branding is all about geese flying in the V formation, and how that plays out in business when we align our people to our purpose. I have used Hop-Skip-Jump in the previous site, and now want The Rising Arc @ Task to replace that narrative. The website is colourful, fun, but needs to have a professional look and I am also looking for more audience engagement on the site. I would like to highlight to a professional small to medium size business audience. I would like to highlight my Reedcast, showcase my speaking, and really utilize the metaphor to put me in a category of one in the speaking and consulting world. My present website is www.brambleroute.ca

Since the website is on Squarespace, does it need to be coded?

To be clear, I already have a site on Squarespace, I do not need a new site. For those interested in the project, can we make the changes to my existing site, instead of creating and hosting a new one????

I have a new video which I will be uploading.
Updates

Here is the link to the video that I need on my website https://qv.example/Tr8mPz2a

Target Market(s)

Small to medium size businesses -

Industry/Entity Type

Business Consulting, Coaching, Speaking

Number of Pages Required

5+ page

Font styles to use
Other font styles liked:
• Calibri, Marydale, Futura

Requirements
Must have
• Color, fun, and showcase The rising arc @ task. It must have my video, Reedcast, and a place for people to want to engage. My case study and e-book to download. Logo's of companies that I have worked with
Nice to have
• A place for people to engage with the site. Testimonials from clients. Copy or video.
Should not have
• A traditional or boring look

```html
<!DOCTYPE html>
<html lang="en">
<head>
<meta charset="utf-8">
<title>Bramble Route Solutions</title>
<link href="https://fonts.googleapis.com/css2?family=Jost:wght@400;500;600;700&family=Open+Sans:wght@400;600;700&family=Shadows+Into+Light&display=swap" rel="stylesheet">
<style>
:root{
  --orange:#f7941d;--sky:#29abe2;--yellow:#f5c400;--green:#3aa55a;--magenta:#c2185b;
  --navy:#2a5d8a;--blue:#3a7fc1;--ink:#1c1c1c;--text:#444;--muted:#999;--grey:#f0f0f0;
  --footer:#262626;--red:#e53935;--white:#fff;
}
*{margin:0;padding:0;box-sizing:border-box}
html,body{width:1200px;height:4955px;overflow:hidden}
body{position:relative;background:var(--white);font-family:"Open Sans",Arial,sans-serif;color:var(--text)}
.abs{position:absolute}
.script{font-family:"Shadows Into Light",cursive;color:var(--navy);font-size:23px;line-height:1}
.title{font-family:"Jost",Helvetica,sans-serif;font-weight:700;color:var(--ink);font-size:31px;line-height:1.1;text-transform:uppercase}
.center{text-align:center;left:0;width:1200px}
.btn{position:absolute;display:flex;align-items:center;justify-content:center;border-radius:20px;color:#fff;font-family:"Jost",sans-serif;font-weight:600;font-size:11px;text-transform:uppercase;letter-spacing:.3px}
.para{font-size:11.5px;line-height:20px;color:var(--text)}
.ph{position:absolute}

/* hero */
.hero{left:0;top:0;width:1200px;height:600px;background:linear-gradient(90deg,#1f2b3a 0%,#3a4656 35%,#7a8590 60%,#b9aea2 80%,#8c7d70 100%)}
.brand{left:110px;top:18px;width:80px;text-align:center;color:#fff}
.brand .mark{width:54px;height:54px;border-radius:50%;background:#fff;margin:0 auto 4px}
.brand span{font-family:"Jost",sans-serif;font-weight:700;font-size:7px;letter-spacing:.5px;display:block;line-height:1.2}
.menu-dot{left:914px;top:38px;width:38px;height:38px;border-radius:50%;background:rgba(255,255,255,.3);display:flex;flex-direction:column;justify-content:center;align-items:center;gap:4px}
.menu-dot i{display:block;width:16px;height:2px;background:#fff}
.hero-script{left:112px;top:190px;color:#fff;font-size:34px}
.hero-title{left:112px;top:230px;font-family:"Jost",sans-serif;font-weight:700;font-size:45px;line-height:47px;color:#fff;text-transform:uppercase}
.hero-title b{color:var(--yellow);font-weight:700}

/* about */
.about-photo{left:210px;top:667px;width:302px;height:358px;background:linear-gradient(135deg,#8a4a3a,#b86a4c 45%,#c99060 70%,#6a4a60)}
.about-text{left:585px;top:706px;width:420px}

/* together */
.together{left:0;top:1092px;width:1200px;height:787px;background:var(--grey)}
.card{position:absolute;top:1390px;width:246px;height:421px;background:#fff;box-shadow:0 4px 14px rgba(0,0,0,.08);text-align:center}
.card .img{height:160px}
.card .icon{position:absolute;left:90px;top:127px;width:66px;height:66px;border-radius:50%;border:4px solid #fff}
.card .label{margin-top:50px;font-family:"Shadows Into Light",cursive;font-size:13px;letter-spacing:.5px}
.card h3{font-family:"Jost",sans-serif;font-weight:700;font-size:21px;color:var(--ink);margin:6px 0 10px}
.card p{font-size:10.5px;line-height:18px;padding:0 22px;color:var(--text);height:90px}
.card a{display:inline-block;margin-top:14px;font-family:"Jost",sans-serif;font-weight:700;font-size:10.5px;text-decoration:underline}

/* video */
.video{left:560px;top:1948px;width:528px;height:319px;background:#111;border-radius:4px;overflow:hidden}
.video .frame{position:absolute;left:0;top:0;width:528px;height:290px;background:linear-gradient(90deg,#1b1b1b,#3a2f2a 40%,#5a4a44 55%,#1e1e1e)}
.video .name{position:absolute;left:360px;top:127px;color:#fff;font-family:"Jost",sans-serif;font-size:12px;letter-spacing:3px;font-weight:600;border-left:2px solid #fff;padding-left:14px}
.video .bar{position:absolute;left:0;top:290px;width:528px;height:29px;background:#111}

/* testimonials */
.testi{left:0;top:2333px;width:1200px;height:551px;background:var(--grey)}
.tcard{position:absolute;background:#fff}
.quote{font-family:"Jost",sans-serif;font-size:9.5px;line-height:15px;color:#555}
.logo-name{font-family:"Jost",sans-serif;font-weight:700;color:var(--navy)}

/* podcast */
.pod-bg{left:0;top:3503px;width:1200px;height:631px;background:var(--grey)}
.pod{position:absolute;left:131px;width:938px;height:124px;background:#fff}
.pod .thumb{position:absolute;left:14px;top:14px;width:138px;height:96px;background:linear-gradient(135deg,#4a3a30,#c07040 60%,#2a2a2a)}
.pod .meta{position:absolute;left:185px;top:20px;font-family:"Jost",sans-serif}
.pod .who{font-size:10px;color:var(--muted)}
.pod .show{font-size:11px;font-weight:700;color:var(--ink);margin-top:6px}
.pod .ep{font-size:8.5px;color:#bbb;margin-top:10px}
.pod .len{font-size:11px;font-weight:600;color:var(--ink);margin-top:6px}
.pod .play{position:absolute;left:438px;top:40px;width:44px;height:44px;border-radius:50%;border:2px solid #ddd;background:#fff}
.pod .track{position:absolute;left:560px;top:83px;width:170px;height:3px;background:#eee}
.pod .track i{position:absolute;left:0;top:0;width:86px;height:3px;background:var(--yellow)}
.pod .track b{position:absolute;left:84px;top:-3px;width:8px;height:8px;border-radius:50%;background:#333}
.pod .vol{position:absolute;left:746px;top:37px;width:60px;height:2px;background:#333}
.pod .time{position:absolute;left:560px;top:30px;font-size:8px;color:#bbb}
.pod .c1,.pod .c2{position:absolute;left:880px;width:32px;height:32px;border-radius:50%}
.pod .c1{top:18px}
.pod .c2{top:58px;background:#eee}

/* logos */
.logo-box{position:absolute;top:4205px;width:175px;height:116px;background:#fff;box-shadow:0 3px 14px rgba(0,0,0,.1);display:flex;align-items:center;justify-content:center;text-align:center;font-family:"Jost",sans-serif;font-weight:600;font-size:18px;color:#333;padding:0 10px}

/* club */
.footer{left:0;top:4510px;width:1200px;height:445px;background:var(--footer)}
.club{left:110px;top:4384px;width:978px;height:244px;background:var(--yellow);border-radius:6px;text-align:center}
.club .input{position:absolute;left:223px;top:150px;width:532px;height:48px;background:#fff;border:3px solid #fff;box-shadow:0 0 0 2px rgba(255,255,255,.6)}
.club .input span{position:absolute;left:20px;top:14px;font-size:10px;color:#333}
.club .input .go{position:absolute;right:0;top:0;width:106px;height:42px;background:#2b6cb0;color:#fff;font-family:"Jost",sans-serif;font-weight:700;font-size:9px;display:flex;align-items:center;justify-content:center}
.fcol{position:absolute;top:4700px;color:#ccc;font-size:10.5px;line-height:21px}
.fcol h4{font-family:"Jost",sans-serif;font-weight:600;color:#fff;font-size:13px;letter-spacing:1.5px;margin-bottom:14px}
.social{position:absolute;top:4826px;width:24px;height:24px;border-radius:50%}
</style>
</head>
<body>

<!-- HERO -->
<section class="abs hero" role="img" aria-label="Photo of two smiling colleagues working together at a laptop"></section>
<div class="abs brand"><div class="mark"></div><span>BRAMBLE ROUTE</span><span>SOLUTIONS</span></div>
<div class="abs menu-dot"><i></i><i></i><i></i></div>
<div class="btn" style="left:962px;top:38px;width:126px;height:35px;background:var(--orange)">Get Started</div>
<div class="abs script hero-script">Companies Are Reaping</div>
<h1 class="abs hero-title">The <b>Benefits</b><br><b>of Bramble Route</b><br>Solutions'<br>Unique Approach</h1>
<div class="btn" style="left:112px;top:444px;width:134px;height:37px;background:var(--sky)">Get Started</div>

<!-- ABOUT -->
<div class="ph about-photo" role="img" aria-label="Portrait of the CEO in a colourful patterned shirt against a brick wall"></div>
<div class="abs about-text">
  <div class="script">History of Ceo</div>
  <h2 class="title" style="margin:6px 0 12px">About Dalton Pryce</h2>
  <p class="para">Sometimes known as the "strivescale guy," dalton has quickly<br>become recognized for being the "hop, skip, jump guy." an award-winning<br>pioneer in the field of human resources, dalton studies the implications of<br>counter-intuitive work environments on individuals and organizations as a whole.<br>dalton brings insights to employees, employers, and human resource<br>professionals alike which leads to harmony, productivity,<br>and profitability.</p>
</div>
<div class="btn" style="left:585px;top:946px;width:119px;height:35px;background:var(--green)">Lear More</div>

<!-- TOGETHER -->
<section class="abs together"></section>
<div class="abs script center" style="top:1150px">The rising arc @ task</div>
<h2 class="abs title center" style="top:1184px">We're Better Together.</h2>
<p class="abs center" style="top:1238px;font-size:12px;line-height:20px;font-weight:600;color:#333">At Bramble Route Solutions, we believe everyone has a place. We can all work together to<br>achieve organizational goals and find self-fulfillment.</p>
<p class="abs center para" style="top:1292px;font-size:11.5px">Sometimes, team members stand out in a way that is awkward for the team. Sometimes, it is us who<br>feel as though we don't belong. The truth is, from time to time, we all feel like the odd one out.</p>
<p class="abs center" style="top:1344px;font-size:10px;font-weight:700;color:var(--orange)">IF YOU'RE FEELING LIKE A MISFIT, THE GOOSE IN A POND FULL OF DUCKS, YOU'RE NOT ALONE.</p>

<article class="card" style="left:210px">
  <div class="img" role="img" aria-label="Geese flying over water at sunset" style="background:linear-gradient(180deg,#c08a4a,#e0a860 55%,#5a6a70)"></div>
  <div class="icon" style="background:var(--blue)"></div>
  <div class="label" style="color:var(--blue)">INDIVIDUALS</div>
  <h3>Goose</h3>
  <p>Do you feel like a misfit?<br>feel like you aren't contributing to your full potential? that you are flying outside the "v" and bucking a headwind feeling tired and frustrated?</p>
  <a style="color:var(--blue)">LEARN MORE</a>
</article>
<article class="card" style="left:477px">
  <div class="img" role="img" aria-label="Flock of geese in flight in warm light" style="background:linear-gradient(180deg,#6a5a48,#b89a70 50%,#d8b88a)"></div>
  <div class="icon" style="background:var(--green)"></div>
  <div class="label" style="color:var(--magenta)">TEAMS</div>
  <h3>Flock</h3>
  <p>Every organization has teams of people that work together to contribute to the whole. each team is dynamic, and has its own goals of what needs to be accomplished.</p>
  <a style="color:var(--green)">LEARN MORE</a>
</article>
<article class="card" style="left:742px">
  <div class="img" role="img" aria-label="Mountain lake reflecting peaks at dawn" style="background:linear-gradient(180deg,#2a4a70,#c87a40 45%,#3a6a8a)"></div>
  <div class="icon" style="background:var(--magenta)"></div>
  <div class="label" style="color:var(--blue)">ORGANIZATIONS</div>
  <h3>Pond</h3>
  <p>Are you the leader of the organization? you are responsible for the individual geese, the flocks, and the entire pond. you see the pond differently. you get to fly over at altitude</p>
  <a style="color:var(--magenta)">LEARN MORE</a>
</article>

<!-- VIDEO -->
<div class="abs" style="left:110px;top:2000px;width:400px">
  <div class="script">Speaking</div>
  <h2 class="title" style="margin:6px 0 12px">Our Video</h2>
  <p class="para" style="line-height:26px">Watch dalton pryce in action as he walks you through the<br>benefits of strivescale and how it can completely restructure your<br>workplace dynamics.</p>
</div>
<div class="btn" style="left:110px;top:2177px;width:132px;height:34px;background:var(--magenta)">Watch Now</div>
<div class="abs video">
  <div class="frame" role="img" aria-label="Video still of the speaker in a patterned shirt on a dark stage"></div>
  <div class="name">DALTON PRYCE</div>
  <svg class="abs" style="left:241px;top:122px" width="44" height="44" viewBox="0 0 44 44"><circle cx="22" cy="22" r="21" fill="#f5c400"/><path d="M17 13 L31 22 L17 31 Z" fill="#fff"/></svg>
  <div class="bar">
    <div class="abs" style="left:0;top:0;width:528px;height:3px;background:#333"></div>
    <div class="abs" style="left:0;top:0;width:330px;height:3px;background:#5a5ae0"></div>
    <svg class="abs" style="left:8px;top:10px" width="60" height="10"><path d="M0 0 L7 5 L0 10Z" fill="#ddd"/><rect x="20" y="2" width="8" height="6" fill="#888"/><rect x="40" y="2" width="8" height="6" fill="#888"/></svg>
    <span class="abs" style="left:240px;top:9px;font-size:7px;color:#aaa">02:18 / 05:12</span>
    <span class="abs" style="left:470px;top:9px;font-size:7px;color:#aaa">1080p HD</span>
  </div>
</div>

<!-- TESTIMONIALS -->
<section class="abs testi"></section>
<div class="abs script center" style="top:2398px">My case study</div>
<h2 class="abs title center" style="top:2426px">Our Clients Say About Us</h2>

<div class="tcard" style="left:0;top:2515px;width:273px;height:212px">
  <div class="abs" style="left:0;top:0;width:26px;height:212px;background:#d9d0c4" role="img" aria-label="Client photo edge"></div>
  <div class="abs logo-name" style="left:70px;top:38px;font-size:15px">CRESTLINE</div>
  <p class="abs quote" style="left:58px;top:78px;width:190px;font-size:8px;line-height:12px">Lorem ipsum dolor sit amet, consectetur adipiscing elit. Pellentesque nibh sem, facilisis feugiat lacus mollis, aliquet aliquam eros. Proin vel nunc venenatis nisi feugiat viverra.</p>
  <p class="abs quote" style="left:70px;top:146px;font-size:8px;font-weight:600">-Mira Okafor</p>
  <div class="abs" style="left:70px;top:172px;width:100px;height:20px;border:1px solid #8a7ad0;border-radius:10px;font-size:7px;color:#8a7ad0;text-align:center;line-height:18px">VIEW CASE STUDY</div>
</div>

<div class="tcard" style="left:300px;top:2488px;width:598px;height:212px">
  <div class="abs" style="left:0;top:0;width:298px;height:212px;background:linear-gradient(135deg,#e8e2d8,#c8b8a0 50%,#7a8a9a)" role="img" aria-label="Portrait of a smiling client holding a mug"></div>
  <div class="abs logo-name" style="left:346px;top:38px;font-size:18px"><span style="display:inline-block;width:14px;height:14px;border-radius:50%;background:var(--navy);vertical-align:-1px;margin-right:6px"></span>Birch Hollow</div>
  <p class="abs quote" style="left:346px;top:96px;width:230px">Lorem ipsum dolor sit amet, consectetur adipiscing elit. Pellentesque nibh sem, facilisis feugiat lacus mollis, aliquet aliquam eros. Proin vel nunc venenatis nisi feugiat viverra.</p>
  <p class="abs quote" style="left:346px;top:180px;font-weight:700">-Mira Okafor</p>
</div>
<div class="abs" style="left:646px;top:2700px;width:124px;height:28px;border:1.5px solid #8a7ad0;border-radius:14px;font-family:Jost,sans-serif;font-size:9px;font-weight:600;color:#6a5ac0;text-align:center;line-height:25px;background:#fff">VIEW CASE STUDY</div>

<div class="tcard" style="left:927px;top:2515px;width:273px;height:212px">
  <div class="abs" style="left:0;top:0;width:240px;height:212px;background:linear-gradient(135deg,#eeeae4,#c8b8a8 55%,#d8d2ca)" role="img" aria-label="Client smiling while holding a cup"></div>
</div>
<div class="btn" style="left:488px;top:2788px;width:223px;height:37px;background:var(--orange)">Read More Testimonials</div>

<!-- EBOOK -->
<div class="ph" style="left:236px;top:2948px;width:226px;height:488px;border-radius:22px;background:linear-gradient(160deg,#e8e8e8,#bdbdbd 60%,#dcdcdc)" role="img" aria-label="Tablet showing the e-book cover with a colourful brain graphic"></div>
<div class="abs" style="left:563px;top:3064px;width:430px">
  <div class="script">Electronic book</div>
  <h2 class="title" style="margin:6px 0 14px">E-Book to Download</h2>
  <p class="para" style="font-size:10.5px;line-height:19px">Lorem ipsum dolor sit amet, consectetur adipiscing elit. Quisque maximus lobortis sapien, et condimentum neque vestibulum ac. Mauris vel nibh commodo, malesuada turpis sit amet, porttitor augue. Praesent placerat vulputate faucibus. Aliquam iaculis metus eget aliquet fringilla. Maecenas ultricies, dolor quis porttitor volutpat, nisl erat hendrerit justo, id tincidunt ex nunc vitae dolor. Ut consectetur turpis eget urna placerat, vel tristique ex ornare. Curabitur tortor tortor, porta malesuada justo eget, elementum aliquam risus. Nunc non orci mauris.</p>
</div>
<div class="btn" style="left:563px;top:3302px;width:179px;height:34px;background:var(--navy)">Download the Book</div>

<!-- REEDCAST -->
<section class="abs pod-bg"></section>
<div class="abs script center" style="top:3564px">Speaking</div>
<h2 class="abs title center" style="top:3594px">My Reedcast</h2>

<div class="pod" style="top:3655px">
  <div class="thumb" role="img" aria-label="Episode cover with a laptop and play symbol"></div>
  <div class="meta"><div class="who">Mira Okafor</div><div class="show">REEDCAST WITH JONAS WHITLOCK</div><div class="ep">Episode 1 &nbsp;•&nbsp; Audiotrack</div><div class="len">10.24</div></div>
  <svg class="abs" style="left:404px;top:55px" width="110" height="14"><path d="M10 0 L10 14 L0 7Z M20 0 L20 14 L10 7Z" fill="#222"/><path d="M90 0 L90 14 L100 7Z M100 0 L100 14 L110 7Z" fill="#222"/></svg>
  <div class="play"><svg width="40" height="40"><path d="M16 12 L28 20 L16 28Z" fill="#222"/></svg></div>
  <div class="time">00:00 / 10:24</div>
  <div class="track"><i></i><b></b></div>
  <div class="vol"></div>
  <svg class="abs" style="left:832px;top:31px" width="12" height="12"><path d="M0 4 H3 L7 0 V12 L3 8 H0Z" fill="#222"/></svg>
  <svg class="c1" style="background:var(--blue)" viewBox="0 0 32 32"><path d="M18 11 L13 16 L18 21" stroke="#fff" stroke-width="2" fill="none"/></svg>
  <svg class="c2" viewBox="0 0 32 32"><path d="M14 11 L19 16 L14 21" stroke="#555" stroke-width="2" fill="none"/></svg>
</div>
<div class="pod" style="top:3800px">
  <div class="thumb" role="img" aria-label="Episode cover with a laptop and play symbol"></div>
  <div class="meta"><div class="who">Mira Okafor</div><div class="show">REEDCAST WITH JONAS WHITLOCK</div><div class="ep">Episode 2 &nbsp;•&nbsp; Audiotrack</div><div class="len">10.24</div></div>
  <svg class="abs" style="left:404px;top:55px" width="110" height="14"><path d="M10 0 L10 14 L0 7Z M20 0 L20 14 L10 7Z" fill="#222"/><path d="M90 0 L90 14 L100 7Z M100 0 L100 14 L110 7Z" fill="#222"/></svg>
  <div class="play"><svg width="40" height="40"><path d="M16 12 L28 20 L16 28Z" fill="#222"/></svg></div>
  <div class="time">00:00 / 10:24</div>
  <div class="track"><i></i><b></b></div>
  <div class="vol"></div>
  <svg class="abs" style="left:832px;top:31px" width="12" height="12"><path d="M0 4 H3 L7 0 V12 L3 8 H0Z" fill="#222"/></svg>
  <svg class="c1" style="background:var(--green)" viewBox="0 0 32 32"><path d="M18 11 L13 16 L18 21" stroke="#fff" stroke-width="2" fill="none"/></svg>
  <svg class="c2" viewBox="0 0 32 32"><path d="M14 11 L19 16 L14 21" stroke="#555" stroke-width="2" fill="none"/></svg>
</div>
<div class="pod" style="top:3946px">
  <div class="thumb" role="img" aria-label="Episode cover with a laptop and play symbol"></div>
  <div class="meta"><div class="who">Mira Okafor</div><div class="show">REEDCAST WITH JONAS WHITLOCK</div><div class="ep">Episode 3 &nbsp;•&nbsp; Audiotrack</div><div class="len">10.24</div></div>
  <svg class="abs" style="left:404px;top:55px" width="110" height="14"><path d="M10 0 L10 14 L0 7Z M20 0 L20 14 L10 7Z" fill="#222"/><path d="M90 0 L90 14 L100 7Z M100 0 L100 14 L110 7Z" fill="#222"/></svg>
  <div class="play"><svg width="40" height="40"><path d="M16 12 L28 20 L16 28Z" fill="#222"/></svg></div>
  <div class="time">00:00 / 10:24</div>
  <div class="track"><i></i><b></b></div>
  <div class="vol"></div>
  <svg class="abs" style="left:832px;top:31px" width="12" height="12"><path d="M0 4 H3 L7 0 V12 L3 8 H0Z" fill="#222"/></svg>
  <svg class="c1" style="background:var(--magenta)" viewBox="0 0 32 32"><path d="M18 11 L13 16 L18 21" stroke="#fff" stroke-width="2" fill="none"/></svg>
  <svg class="c2" viewBox="0 0 32 32"><path d="M14 11 L19 16 L14 21" stroke="#555" stroke-width="2" fill="none"/></svg>
</div>

<!-- PARTNER NAMES -->
<div class="logo-box" style="left:112px">Truewell</div>
<div class="logo-box" style="left:312px;font-size:13px;line-height:16px"><span style="display:inline-block;width:22px;height:22px;border-radius:50%;background:#333;margin-right:8px;flex:none"></span><span style="text-align:left">Ledgerfield<br>Data Group</span></div>
<div class="logo-box" style="left:512px;font-size:22px">Glance Studio</div>
<div class="logo-box" style="left:712px">Civicbyte</div>
<div class="logo-box" style="left:912px">Harlow Homes</div>

<!-- CLUB + FOOTER -->
<footer class="abs footer"></footer>
<div class="abs club">
  <div class="script" style="margin-top:54px;color:#222">Feel like a misfit?</div>
  <h2 class="title" style="margin-top:8px;font-size:30px">Join the Club</h2>
  <p style="font-size:11px;color:#333;margin-top:4px">Sign Up With Your Email Address To Receive News And Updtes.</p>
  <div class="input"><span>Email Address</span><div class="go">SIGN UP</div></div>
</div>

<div class="abs brand" style="left:129px;top:4692px"><div class="mark" style="width:70px;height:70px"></div><span>BRAMBLE ROUTE</span><span>SOLUTIONS</span></div>
<div class="social" style="left:112px;background:#888"></div>
<div class="social" style="left:142px;background:#888"></div>
<div class="social" style="left:172px;background:var(--yellow)"></div>
<div class="social" style="left:202px;background:#888"></div>

<div class="fcol" style="left:348px"><h4>LINKS</h4>Who We Are<br>What We Do<br>Who We Help<br>Media<br>E Book<br>#riseinthearc</div>
<div class="fcol" style="left:567px"><h4>LEGAL</h4>Ready To Soar?<br>#riseinthearc<br>Find Your Way<br>Terms &amp; Conditions<br>Privacy Policy</div>
<div class="fcol" style="left:810px"><h4>NEWSLETTER</h4>Sign Up With Your Email Address To<br>Receive News And Updtes.</div>
<div class="abs" style="left:811px;top:4796px;width:277px;height:34px;border:1px solid #fff;background:#fff">
  <span class="abs" style="left:12px;top:10px;font-size:9px;color:#333">Email Address</span>
  <div class="abs" style="right:0;top:0;width:82px;height:32px;background:var(--red);color:#fff;font-family:Jost,sans-serif;font-weight:700;font-size:9px;text-align:center;line-height:32px">SIGN UP</div>
</div>
<div class="abs" style="left:110px;top:4884px;width:978px;height:1px;background:#444"></div>
<p class="abs center" style="top:4916px;font-size:11px;color:#ccc">©2023 Bramble Route Solutions | All Rights Reserved</p>

</body>
</html>
```